Willowmere Spa and Beauty Ltd. (Name of business)

I need a business card designed for this new company based out of Toronto Ontario. We specialize in Eyelash Extensions, Manicures and Pedicures, body waxing, massages, laser hair removal and botox treatments. Also offer a variety of products for sale, such as skin cream serums, collagen gel, eye cream, etc. It is a safe relaxing and non-judgemental environnment. Clients are welcome to come be pampered for the half or full day. Many service packages to choose from.

Open 7days per week from 8am to 8pm.

Priscilla Dunmore
Spa Facilitator
Willowmere Spa and Beauty Ltd.
7200 Harcourt St; Suite 1400
Toronto ON K2P 9W4

OFFICE: 416.790.4100
FAX: 416.790.4101
CELL: 416.632.1987
EMAIL: priscilla.dunmore@willowmerespa.com

Target Market(s)

Target market is primarily female ranging from 16 years old to 50 years old.

Industry/Entity Type

Business

Contact Information for Business Card

Priscilla Dunmore
Spa Facilitator
7200 Harcourt St; Suite 1400
Toronto ON K2P 9W4

OFFICE: 416.790.4100
FAX: 416.790.4101
CELL: 416.632.1987

Logo Text

I dont have a logo yet. I would like it simple but sophisticated and modern.

Font styles to use
Serif

Requirements
Must have
• all pertinent details such as company name, logo, name and contact information, services that are offered, including package rates
Nice to have
• Company name and logo prominent. A card that is neat and the information such as address, phone number, fax, email, etc is not too crowded but laid out in an easy to read format.
• Possibly on the back of card - some of the services offered could be listed, as well as professional cream lotions and serums. Hours of operation etc.

```html
<!DOCTYPE html>
<html lang="en">
<head>
<meta charset="utf-8">
<title>Willowmere Spa and Beauty Ltd. — Business Card</title>
<link href="https://fonts.googleapis.com/css2?family=Open+Sans:wght@400;600&family=Parisienne&family=Cormorant+Garamond:wght@500&display=swap" rel="stylesheet">
<style>
  :root {
    --page: #e9e6e1;
    --card-light: #ffffff;
    --card-light-shade: #e4e4e4;
    --card-dark: #2e2e2e;
    --card-dark-deep: #1f1f1f;
    --ink: #1c1c1c;
    --ink-soft: #d9d9d9;
    --teal: #5fbfac;
    --teal-deep: #2d6660;
  }
  * { margin: 0; padding: 0; box-sizing: border-box; }
  html, body { width: 1200px; height: 1200px; overflow: hidden; }
  body {
    background: var(--page);
    font-family: "Open Sans", Arial, sans-serif;
    position: relative;
  }
  .card {
    position: absolute;
    left: 150px;
    width: 900px;
    height: 514px;
    border-radius: 26px;
    box-shadow: 0 10px 28px rgba(0,0,0,.18);
    overflow: hidden;
  }
  .card--front {
    top: 46px;
    background: radial-gradient(ellipse at 40% 45%, var(--card-light) 45%, var(--card-light-shade) 100%);
    color: var(--ink);
  }
  .card--back {
    top: 640px;
    background: radial-gradient(ellipse at 55% 30%, var(--card-dark) 30%, var(--card-dark-deep) 100%);
    color: var(--ink-soft);
  }

  /* brand lockup */
  .brand { position: absolute; display: flex; align-items: center; gap: 18px; }
  .brand__dot { width: 58px; height: 58px; border-radius: 50%; background: var(--teal); flex: none; }
  .brand__name { font-weight: 400; line-height: 1.05; }
  .brand__name .brand__word { display: block; font-size: 44px; letter-spacing: .5px; }
  .brand__name .brand__sub { display: block; font-size: 17px; letter-spacing: .6px; margin-top: 4px; }
  .card--front .brand { left: 70px; top: 222px; }
  .card--front .brand__name { color: var(--ink); }
  .card--back .brand { right: 70px; top: 92px; }
  .card--back .brand__name { color: var(--ink-soft); }

  /* person */
  .person { position: absolute; left: 460px; top: 62px; }
  .person__name { font-family: "Parisienne", cursive; font-size: 50px; line-height: 1; color: var(--ink); }
  .person__title { font-family: "Cormorant Garamond", Georgia, serif; font-size: 27px; color: var(--teal); margin: 2px 0 0 78px; }

  /* contacts */
  .contacts { position: absolute; left: 460px; top: 200px; list-style: none; }
  .contacts li { display: flex; align-items: flex-start; gap: 16px; font-size: 20px; line-height: 1.3; margin-bottom: 12px; }
  .contacts svg { width: 22px; height: 22px; flex: none; margin-top: 3px; fill: var(--teal); }

  /* back lists */
  .offer { position: absolute; left: 64px; top: 44px; }
  .offer__heading { color: var(--teal); font-size: 21px; margin-bottom: 8px; }
  .offer__heading + .offer__list { margin-bottom: 20px; }
  .offer__list { list-style: none; }
  .offer__list li { display: flex; align-items: center; gap: 10px; font-size: 20px; line-height: 1.55; }
  .offer__list svg { width: 20px; height: 20px; flex: none; stroke: var(--ink-soft); fill: none; stroke-width: 1.6; }
  .hours { position: absolute; right: 64px; bottom: 52px; color: var(--teal); font-size: 20px; }
</style>
</head>
<body>

<section class="card card--front" aria-label="Front of business card">
  <div class="brand">
    <span class="brand__dot"></span>
    <span class="brand__name"><span class="brand__word">Willowmere</span><span class="brand__sub">Spa and Beauty Ltd.</span></span>
  </div>

  <div class="person">
    <p class="person__name">Priscilla Dunmore</p>
    <p class="person__title">Spa Facilitator</p>
  </div>

  <ul class="contacts">
    <li>
      <svg viewBox="0 0 24 24" aria-hidden="true"><path d="M12 2a7 7 0 0 0-7 7c0 5 7 13 7 13s7-8 7-13a7 7 0 0 0-7-7zm0 9.5A2.5 2.5 0 1 1 12 6.5a2.5 2.5 0 0 1 0 5z"/></svg>
      <span>7200 Harcourt St; Suite 1400<br>Toronto ON K2P 9W4</span>
    </li>
    <li>
      <svg viewBox="0 0 24 24" aria-hidden="true"><path d="M2 9c0-3 4-5 10-5s10 2 10 5v2h-5V8H7v3H2zm4 4h12l2 8H4zm6 1.5a3 3 0 1 0 0 6 3 3 0 0 0 0-6z"/></svg>
      <span>416.790.4100</span>
    </li>
    <li>
      <svg viewBox="0 0 24 24" aria-hidden="true"><path d="M7 3h8l3 3v4H7zM3 11h18v9H3zm3 3v2h3v-2zm6 0v2h6v-2z"/></svg>
      <span>416.790.4101</span>
    </li>
    <li>
      <svg viewBox="0 0 24 24" aria-hidden="true"><path d="M7 1h10a2 2 0 0 1 2 2v18a2 2 0 0 1-2 2H7a2 2 0 0 1-2-2V3a2 2 0 0 1 2-2zm0 3v14h10V4zm5 15.5a1 1 0 1 0 0 2 1 1 0 0 0 0-2z"/></svg>
      <span>416.632.1987</span>
    </li>
    <li>
      <svg viewBox="0 0 24 24" aria-hidden="true"><path d="M2 5h20v14H2zm2 2v.5l8 5.5 8-5.5V7z"/></svg>
      <span>priscilla.dunmore@willowmerespa.com</span>
    </li>
  </ul>
</section>

<section class="card card--back" aria-label="Back of business card">
  <div class="offer">
    <p class="offer__heading">We specialize in</p>
    <ul class="offer__list">
      <li><svg viewBox="0 0 20 20" aria-hidden="true"><rect x="2" y="5" width="12" height="12"/><path d="M5 10l3 3 9-10"/></svg>Eyelash Extensions</li>
      <li><svg viewBox="0 0 20 20" aria-hidden="true"><rect x="2" y="5" width="12" height="12"/><path d="M5 10l3 3 9-10"/></svg>Manicures and Pedicures</li>
      <li><svg viewBox="0 0 20 20" aria-hidden="true"><rect x="2" y="5" width="12" height="12"/><path d="M5 10l3 3 9-10"/></svg>body waxing</li>
      <li><svg viewBox="0 0 20 20" aria-hidden="true"><rect x="2" y="5" width="12" height="12"/><path d="M5 10l3 3 9-10"/></svg>massages</li>
      <li><svg viewBox="0 0 20 20" aria-hidden="true"><rect x="2" y="5" width="12" height="12"/><path d="M5 10l3 3 9-10"/></svg>laser hair removal and botox treatments</li>
    </ul>
    <p class="offer__heading">We offer variety of products for sale</p>
    <ul class="offer__list">
      <li><svg viewBox="0 0 20 20" aria-hidden="true"><rect x="2" y="5" width="12" height="12"/><path d="M5 10l3 3 9-10"/></svg>skin cream serums</li>
      <li><svg viewBox="0 0 20 20" aria-hidden="true"><rect x="2" y="5" width="12" height="12"/><path d="M5 10l3 3 9-10"/></svg>collagen gel</li>
      <li><svg viewBox="0 0 20 20" aria-hidden="true"><rect x="2" y="5" width="12" height="12"/><path d="M5 10l3 3 9-10"/></svg>eye cream,</li>
    </ul>
  </div>

  <div class="brand">
    <span class="brand__dot"></span>
    <span class="brand__name"><span class="brand__word">Willowmere</span><span class="brand__sub">Spa and Beauty Ltd.</span></span>
  </div>

  <p class="hours">Open 7days per week from 8am to 8pm</p>
</section>

</body>
</html>
```